Real Estate Business Cards

Looking for a clean, sharp and professional look for our Real Estate investment Fund that invests in Multi Family Apartment buildings.

Target Market(s)

Real Estate Fund

Industry/Entity Type

Real Estate

Contact Information for Business Card

Company Description: Real Estate Investment Fund
Company Name: KRV Holdings
Name: Marcus Tovell
Cell: (917) 482-0957
Email: marcus@krvholdings-example.com
Website: www.krvholdings-example.com
Address: 148, 7th Street, Brooklyn NY 11217

Colors

Designer to choose colors to be used in the design.

Requirements
Nice to have
• Colors to match logo

```html
<!DOCTYPE html>
<html lang="en">
<head>
<meta charset="utf-8">
<title>KRV Holdings – Business Card</title>
<link href="https://fonts.googleapis.com/css2?family=Libre+Baskerville&family=Lato:wght@400&display=swap" rel="stylesheet">
<style>
  :root {
    --backdrop: #2a2a2a;
    --card-white: #ffffff;
    --brand-blue: #1272aa;
    --slate: #4a4a4a;
    --ink: #3d3d3d;
    --rule: #b5b5b5;
  }
  * { margin: 0; padding: 0; box-sizing: border-box; }
  html, body { width: 1200px; height: 1200px; overflow: hidden; }
  body { background: var(--backdrop); position: relative; font-family: "Lato", sans-serif; }

  .card {
    position: absolute; top: 310px; width: 366px; height: 594px;
    box-shadow: 0 4px 10px rgba(0,0,0,0.55);
  }
  .card--front { left: 233px; background: var(--card-white); text-align: center; }
  .card--back { left: 628px; background: var(--slate); overflow: hidden; }

  .brand-square {
    position: absolute; left: 143px; top: 108px; width: 80px; height: 80px;
    background: var(--brand-blue);
  }
  .brand-name {
    position: absolute; left: 0; right: 0; top: 226px;
    font-family: "Libre Baskerville", serif; font-size: 31px; letter-spacing: 1px;
    color: var(--brand-blue);
  }
  .person-name {
    position: absolute; left: 0; right: 0; top: 348px;
    font-family: "Libre Baskerville", serif; font-size: 22px; color: var(--brand-blue);
  }
  .contact-icons { position: absolute; left: 100px; top: 389px; }
  .contact-list {
    position: absolute; left: 0; right: 0; top: 424px;
    font-size: 16.5px; line-height: 21.5px; color: var(--ink);
  }
  .contact-rule {
    position: absolute; left: 101px; width: 170px; top: 500px;
    border-top: 1px solid var(--rule);
  }
  .address {
    position: absolute; left: 0; right: 0; top: 511px;
    font-size: 16.5px; line-height: 21.5px; color: var(--ink); font-style: normal;
  }

  .back-art { position: absolute; inset: 0; }
  .back-name {
    position: absolute; left: 0; right: 0; top: 430px; text-align: center;
    font-family: "Libre Baskerville", serif; font-size: 26px; letter-spacing: 2px;
    color: var(--card-white);
  }
</style>
</head>
<body>
  <section class="card card--front">
    <div class="brand-square" aria-hidden="true"></div>
    <h1 class="brand-name">KRV HOLDINGS</h1>
    <h2 class="person-name">MARCUS TOVELL</h2>

    <svg class="contact-icons" width="166" height="24" viewBox="0 0 166 24" aria-hidden="true">
      <line x1="0" y1="12" x2="42" y2="12" stroke="#8a8a8a" stroke-width="1"/>
      <line x1="124" y1="12" x2="166" y2="12" stroke="#8a8a8a" stroke-width="1"/>
      <circle cx="56" cy="12" r="12" fill="var(--brand-blue)"/>
      <circle cx="83" cy="12" r="12" fill="var(--brand-blue)"/>
      <circle cx="110" cy="12" r="12" fill="var(--brand-blue)"/>
      <!-- phone -->
      <path d="M49 10 q7 -5 14 0 v2 h-3 v-2 h-8 v2 h-3z M51 13 h10 l1 5 h-12z" fill="#fff"/>
      <!-- envelope -->
      <rect x="76" y="7" width="14" height="10" rx="1" fill="#fff"/>
      <path d="M76 8 l7 5 l7 -5" fill="none" stroke="var(--brand-blue)" stroke-width="1.2"/>
      <!-- globe -->
      <circle cx="110" cy="12" r="6.5" fill="#fff"/>
      <path d="M110 5.5 v13 M103.5 12 h13 M110 5.5 q-4 6.5 0 13 M110 5.5 q4 6.5 0 13" fill="none" stroke="var(--brand-blue)" stroke-width="1"/>
    </svg>

    <p class="contact-list">
      (917) 482-0957<br>
      marcus@krvholdings-example.com<br>
      www.krvholdings-example.com
    </p>
    <div class="contact-rule"></div>
    <address class="address">
      148, 7th Street<br>
      Brooklyn NY 11217
    </address>
  </section>

  <section class="card card--back">
    <svg class="back-art" width="366" height="594" viewBox="0 0 366 594" aria-hidden="true">
      <polygon points="0,0 45,0 313,268 0,582" fill="var(--brand-blue)"/>
      <rect x="133" y="260" width="100" height="100" rx="10" fill="var(--card-white)"/>
    </svg>
    <p class="back-name">KRV HOLDINGS</p>
  </section>
</body>
</html>
```